Eye-Catching Canva Template for Medical Conference Announcements

I need an eye-catching 4:5 (1080 x 1350 px) Canva template to announce upcoming conferences our team at KORA LUMEN TX will be attending.
The design should reflect our company branding—please use our website (https://koralumentx.example/) and attached logos for reference. It should be modern, bold, and professional, as the audience is pain management physicians.
The first version will be for the NFRQB conference (https://nfrqb.example/), happening in Orlando, FL from May 15–17, 2025. Our booth number is 317.

```html
<!DOCTYPE html>
<html lang="en">
<head>
<meta charset="utf-8">
<title>NFRQB Conference – KORA LUMEN TX</title>
<link rel="stylesheet" href="https://fonts.googleapis.com/css2?family=Inter:wght@700;800&family=Source+Serif+4:opsz,wght@8..60,700&display=swap">
<style>
  :root {
    --bg: #000000;
    --violet: #8f5bf5;
    --white: #ffffff;
    --wave-a: #6a4fd8;
    --wave-b: #3a3f9e;
    --hand-a: #3b6fe0;
    --hand-b: #d65bd8;
    --hand-c: #f08a7a;
  }
  * { margin: 0; padding: 0; box-sizing: border-box; }
  html, body { width: 960px; height: 1200px; overflow: hidden; background: var(--bg); }
  .poster { position: relative; width: 960px; height: 1200px; background: var(--bg); overflow: hidden; }

  .wave-decoration {
    position: absolute; left: 0; top: 0; width: 760px; height: 350px;
    background: radial-gradient(ellipse 60% 55% at 25% 30%, rgba(106,79,216,0.45), rgba(58,63,158,0.18) 55%, transparent 75%);
  }

  .event-name {
    position: absolute; right: 46px; top: 152px;
    font: 800 102px/1 "Inter", sans-serif; letter-spacing: -0.02em;
    color: var(--violet);
  }
  .event-type {
    position: absolute; right: 46px; top: 250px;
    font: 700 107px/1 "Source Serif 4", serif; letter-spacing: -0.02em;
    color: var(--white);
  }
  .divider {
    position: absolute; left: 200px; top: 424px; width: 580px; height: 2px;
    background: var(--violet);
  }
  .event-details {
    position: absolute; left: 202px; top: 453px;
    font: 700 105px/105px "Inter", sans-serif; letter-spacing: -0.035em;
    color: var(--violet);
  }
  .booth {
    position: absolute; left: 201px; top: 790px;
    font: 700 36px/1 "Source Serif 4", serif; letter-spacing: -0.01em;
    color: var(--white);
  }

  .hand-illustration {
    position: absolute; left: 551px; top: 827px; width: 409px; height: 373px;
    background: radial-gradient(ellipse 70% 65% at 60% 60%, rgba(214,91,216,0.6), rgba(59,111,224,0.45) 50%, transparent 78%);
  }

  .brand-name {
    position: absolute; left: 58px; top: 1068px;
    font: 700 44px/1 "Inter", sans-serif; letter-spacing: 0.01em;
    color: var(--white);
  }
</style>
</head>
<body>
  <main class="poster">
    <div class="wave-decoration" role="img" aria-label="Flowing violet dotted wave pattern"></div>

    <h1 class="event-name">NFRQB</h1>
    <h2 class="event-type">Conference</h2>

    <div class="divider"></div>

    <p class="event-details">Orlando, FL<br>May 15-17<br>2025</p>
    <p class="booth">Booth number 317</p>

    <div class="hand-illustration" role="img" aria-label="Glowing blue and pink X-ray style illustration of a hand skeleton"></div>

    <div class="brand-name">KORA LUMEN TX</div>
  </main>
</body>
</html>
```